A Flyer for a clinic/hospital waiting room to warn about patients that they must not abuse our staff

we need a flyer (text attached) with a background of a female nurse or medical doctor photo. I like the example photo where there are four headless satff lined up - something like this, indicating that we are a team and will not tolerate abuse
A4
the text will be over the photo.

Target Market(s)

patients who come to our clinic

Industry/Entity Type

medicine - urology

Colors
0054AA
0677BA
7BADD7
CADEEF
E8F1F8
0094D4
00A9DD
6FCCEA
C7EBF8
E9F6FB

Requirements
Must have
• a photo taking up the whole A4, and text over this. The photos I haev sent are just examples - I will need yo to source a photo
Nice to have
• Horizontal A4 and vertical A4 options. Please add our logo in small , in the bottom right corner

```html
<!DOCTYPE html>
<html lang="en">
<head>
<meta charset="utf-8">
<title>Zero-Tolerance Notice</title>
<link href="https://fonts.googleapis.com/css2?family=Montserrat:wght@400;500;600;900&display=swap" rel="stylesheet">
<style>
  :root {
    --backdrop: #03234a;
    --ink: #1a1a1a;
    --accent: #5a9fd8;
    --accent-rule: #4f97d3;
    --accent-shadow: #1d3550;
    --scrub-blue: #a9c4e2;
    --scrub-light: #cfdff0;
    --paper: #f5f7fa;
    --logo-grey: #5d6670;
  }
  * { margin: 0; padding: 0; box-sizing: border-box; }
  html, body {
    width: 1200px; height: 1200px; overflow: hidden;
    background: var(--backdrop);
    font-family: "Montserrat", sans-serif;
    color: var(--ink);
  }
  .flyer {
    position: absolute; left: 49px; top: 207px;
    width: 1101px; height: 785px;
    background: var(--paper);
    overflow: hidden;
  }
  .flyer-photo {
    position: absolute; inset: 0;
    background:
      linear-gradient(90deg, var(--scrub-blue) 0%, var(--scrub-light) 35%, rgba(240,244,249,0.9) 55%, var(--paper) 75%),
      var(--paper);
  }
  .content {
    position: absolute; left: 468px; top: 0; width: 606px;
  }
  .lead-in {
    position: absolute; top: 28px; left: 0; white-space: nowrap;
    font-size: 30px; font-weight: 500; letter-spacing: 0.1px;
  }
  .headline {
    position: absolute; top: 66px; left: 0; white-space: nowrap;
    font-size: 51px; font-weight: 900; letter-spacing: -0.6px;
    line-height: 1.1;
    color: var(--accent);
    text-shadow: 2px 2px 0 var(--accent-shadow);
  }
  .tagline {
    position: absolute; top: 134px; left: 0; white-space: nowrap;
    font-size: 17.8px; font-weight: 500;
  }
  .rule {
    position: absolute; top: 168px; left: 0; width: 603px; height: 4px;
    background: var(--accent-rule);
  }
  .intro {
    position: absolute; top: 186px; left: 0; white-space: nowrap;
    font-size: 15.5px;
  }
  .behaviours {
    position: absolute; top: 218px; left: 85px; list-style: none;
  }
  .behaviours li {
    font-size: 16px; font-weight: 600; line-height: 26.8px;
    white-space: nowrap; position: relative; padding-left: 14px;
  }
  .behaviours li::before {
    content: ""; position: absolute; left: 0; top: 10px;
    width: 7px; height: 7px; border-radius: 50%; background: var(--accent);
  }
  .notice {
    position: absolute; left: 0; width: 606px;
    font-size: 15.3px; line-height: 23px; text-align: justify;
    text-align-last: left;
  }
  .notice-support { top: 420px; }
  .notice-charges { top: 510px; }
  .notice-reason { top: 572px; }
  .brand {
    position: absolute; right: 29px; bottom: 36px;
    display: flex; align-items: center; gap: 8px;
    font-size: 21px; font-weight: 500; color: var(--logo-grey);
    white-space: nowrap;
  }
  .brand-dot {
    width: 14px; height: 14px; border-radius: 50%; background: var(--accent);
  }
</style>
</head>
<body>
  <main class="flyer">
    <div class="flyer-photo" role="img" aria-label="Photo of a nurse in light blue scrubs with a stethoscope and folded arms, medical team blurred behind, fading to white on the right"></div>
    <section class="content">
      <p class="lead-in">We have zero-tolerance for any form of</p>
      <h1 class="headline">Aggressive behaviour</h1>
      <p class="tagline">Our staff treat you with respect and we expect the same in return.</p>
      <div class="rule"></div>
      <p class="intro">Aggressive behaviour (in-person or on the telephone) is:</p>
      <ul class="behaviours">
        <li>Verbal harassment</li>
        <li>Any verbal or physical confrontation</li>
        <li>Raising your voice or making unreasonable demands</li>
        <li>Abusive or intimidating behaviour</li>
        <li>Sexual or suggestive language or behaviour</li>
        <li>Making threats to our staff</li>
        <li>Swearing</li>
      </ul>
      <p class="notice notice-support">If any of our staff feel intimidated in any way, we will always support them. Incidents will result in your immediate removal from the facility, termination of your relationship with the practice, and may result in prosecution.</p>
      <p class="notice notice-charges">In all circumstances we will support any staff member who wishes to press charges against a perpetrator of aggressive behaviour.</p>
      <p class="notice notice-reason">We take this stance because our staff work extremely hard in busy circumstances to help you and we will no longer tolerate any form of aggression or abuse.</p>
    </section>
    <div class="brand"><span class="brand-dot"></span>Riverbend Urology</div>
  </main>
</body>
</html>
```